Business Card Design & Logo Design

Im a new company selling: balloons, bespoke gift wrapping services & Christmas decorating services i.e. I will come and decorate your tree, wrap your xmas presents, set & decorate your dining table, help you host your xmas party etc. etc.

I don't do 'cheesey' stuff so need a sophisticated card.

I love b&w colours, I love stripes and smart looking stuff.

I do already have an idea and if I don't find anything else then I will go with my idea but would then just need somebody to create the artwork for me.

www.copperwillow.co.uk is currently in the process of being designed so any ideas of logos/designs must also work with a website.

Industry/Entity Type

Business

Contact Information for Business Card

Copper Willow
West Byfleet
KT14 9RD
Surrey
01632 960418
or
07700 900736

treats@copperwillow.co.uk

```html
<!DOCTYPE html>
<html lang="en">
<head>
<meta charset="utf-8">
<title>Copper Willow – Business Card</title>
<link rel="stylesheet" href="https://fonts.googleapis.com/css2?family=Open+Sans:wght@400;600&display=swap">
<style>
  :root {
    --bg: #ecebe8;
    --ink: #1a1a1a;
    --black: #0c0c0c;
    --white: #f7f7f5;
    --pink: #e0157a;
    --stripe-1: #161616;
    --stripe-2: #3c3c3c;
    --stripe-3: #8d8d8d;
    --stripe-4: #5e5e5e;
    --pale-1: #bdbdbd;
    --pale-2: #d3d3d3;
    --pale-3: #a9a9a9;
    --pale-4: #e2e2e2;
    --icon-dark: #cfcfcf;
    --icon-light: #a39c97;
    --label-dark: #e8e8e8;
    --label-light: #8f8883;
  }
  * { box-sizing: border-box; margin: 0; padding: 0; }
  html, body { width: 1200px; height: 723px; overflow: hidden; }
  body {
    background: var(--bg);
    font-family: "Open Sans", Arial, sans-serif;
    display: flex;
    align-items: center;
    justify-content: center;
    gap: 90px;
  }
  .card {
    width: 340px;
    height: 560px;
    display: flex;
    flex-direction: column;
    overflow: hidden;
    box-shadow: 0 6px 18px rgba(0,0,0,.18);
  }

  /* Back: contact side */
  .card--back .contact {
    flex: 0 0 70%;
    background: repeating-linear-gradient(90deg,
      var(--pale-1) 0 22px, var(--pale-2) 22px 40px,
      var(--pale-3) 40px 58px, var(--pale-4) 58px 76px);
    padding: 52px 30px 0;
    color: var(--ink);
  }
  .contact p { font-size: 19px; line-height: 1.3; }
  .contact .address { margin-bottom: 28px; }
  .contact .phones { margin-bottom: 34px; letter-spacing: .5px; }
  .contact .online { font-size: 16px; line-height: 1.6; }
  .contact .web { font-size: 19px; font-weight: 600; }

  .services {
    flex: 1;
    display: flex;
    justify-content: space-around;
    align-items: flex-end;
    padding: 0 14px 22px;
  }
  .card--back .services { background: var(--white); }
  .service { display: flex; flex-direction: column; align-items: center; gap: 8px; }
  .service__icon { width: 58px; height: 70px; border-radius: 6px; }
  .service__label { font-size: 11px; letter-spacing: .5px; text-transform: uppercase; }
  .card--back .service__icon { background: var(--icon-light); opacity: .55; }
  .card--back .service__label { color: var(--label-light); }

  /* Front: brand side */
  .card--front .stripes {
    flex: 0 0 44%;
    background: repeating-linear-gradient(90deg,
      var(--stripe-1) 0 24px, var(--stripe-2) 24px 34px,
      var(--stripe-3) 34px 50px, var(--stripe-4) 50px 60px);
  }
  .brand {
    flex: 0 0 17%;
    background: var(--white);
    position: relative;
    display: flex;
    align-items: center;
    justify-content: center;
  }
  .brand__name {
    color: var(--pink);
    font-size: 34px;
    font-weight: 400;
    margin-top: -12px;
  }
  .brand__rule {
    position: absolute;
    left: 0; right: 0; bottom: 18px;
    height: 3px;
    background: var(--ink);
  }
  .brand__bow {
    position: absolute;
    right: 22px; bottom: 4px;
    width: 52px; height: 32px;
    border-radius: 6px;
    background: var(--pink);
    opacity: .7;
  }
  .card--front .services { background: var(--black); padding-bottom: 30px; }
  .card--front .service__icon { background: var(--icon-dark); opacity: .7; }
  .card--front .service__label { color: var(--label-dark); }
</style>
</head>
<body>

  <section class="card card--back" aria-label="Card back">
    <div class="contact">
      <p class="address">West Byfleet<br>KT14 9RD Surrey</p>
      <p class="phones">01632 960418<br>07700 900736</p>
      <p class="online">treats@copperwillow.co.uk<br><span class="web">www.copperwillow.co.uk</span></p>
    </div>
    <div class="services">
      <div class="service">
        <div class="service__icon" role="img" aria-label="Ornate swirl Christmas tree illustration"></div>
        <span class="service__label">Christmas</span>
      </div>
      <div class="service">
        <div class="service__icon" role="img" aria-label="Patterned round balloon on a string illustration"></div>
        <span class="service__label">Balloons</span>
      </div>
      <div class="service">
        <div class="service__icon" role="img" aria-label="Dotted gift box with bow illustration"></div>
        <span class="service__label">Giftwrap</span>
      </div>
    </div>
  </section>

  <section class="card card--front" aria-label="Card front">
    <div class="stripes"></div>
    <div class="brand">
      <span class="brand__name">Copper Willow</span>
      <div class="brand__rule"></div>
      <div class="brand__bow" role="img" aria-label="Pink ribbon bow ornament"></div>
    </div>
    <div class="services">
      <div class="service">
        <div class="service__icon" role="img" aria-label="Ornate swirl Christmas tree illustration"></div>
        <span class="service__label">Christmas</span>
      </div>
      <div class="service">
        <div class="service__icon" role="img" aria-label="Patterned round balloon on a string illustration"></div>
        <span class="service__label">Balloons</span>
      </div>
      <div class="service">
        <div class="service__icon" role="img" aria-label="Dotted gift box with bow illustration"></div>
        <span class="service__label">Giftwrap</span>
      </div>
    </div>
  </section>

</body>
</html>
```